project - Kestra Nook

Dear designers, I'm Looking for an appealing new business card design to represent us for our new e-cigarette store: The KestrA Nook. Knowledgeable and friendly staff we aim for superior customer service with a positive atmosphere. Classic feel with modern touch is what we are aiming for . Lime green font and grey back round is the original color scheme but we are flexible and open to suggestions. I added some doodles to show you where my mind is at. address: 4308 87 Ave NW Edmonton, AB (inside the hollin trade hall)web: thekestranook.com email: info@thekestranook.com phone : 587.555.0148 Thanks and am looking forward to seeing your creative , fresh and innovative designs.
Good luck everybody!
Jonas
lime green and charcoal grey please. thanks
Business
The KestrA Nook

```html
<!DOCTYPE html>
<html lang="en">
<head>
<meta charset="utf-8">
<title>The KestrA Nook – Business Card</title>
<link rel="stylesheet" href="https://fonts.googleapis.com/css2?family=Quicksand:wght@500;600&display=swap">
<style>
  :root {
    --page: #ffffff;
    --charcoal: #252c2c;
    --charcoal-mist: #2f3737;
    --lime: #b8ff0f;
    --grey: #808080;
    --divider: #7d8080;
    --tagline: #9a9c9c;
  }
  html, body {
    margin: 0;
    padding: 0;
    width: 1200px;
    height: 1000px;
    overflow: hidden;
    background: var(--page);
  }
  .business-card {
    position: absolute;
    left: 57px;
    top: 181px;
    width: 1086px;
    height: 637px;
    background: var(--charcoal);
    overflow: hidden;
    font-family: "Quicksand", sans-serif;
  }
  .smoke-decoration {
    position: absolute;
    left: 115px;
    top: 0;
    width: 230px;
    height: 603px;
    background: radial-gradient(ellipse 55% 50% at 45% 55%, var(--charcoal-mist) 0%, rgba(47,55,55,0.5) 55%, rgba(37,44,44,0) 100%);
  }
  .logo-divider {
    position: absolute;
    left: 459px;
    top: 335px;
    width: 3px;
    height: 242px;
    background: var(--divider);
  }
  .brand-lockup {
    position: absolute;
    right: 114px;
    bottom: 62px;
    max-width: 490px;
    text-align: right;
  }
  .brand-name {
    margin: 0;
    font-size: 60px;
    font-weight: 600;
    line-height: 1;
    letter-spacing: -1.5px;
    color: var(--lime);
    white-space: nowrap;
  }
  .brand-tagline {
    margin: 6px 0 0;
    font-size: 42px;
    font-weight: 500;
    line-height: 1;
    color: var(--tagline);
    white-space: nowrap;
  }
  .footer-band {
    position: absolute;
    left: 0;
    bottom: 0;
    width: 100%;
    height: 34px;
    display: flex;
  }
  .footer-band .accent {
    width: 198px;
    background: var(--lime);
  }
  .footer-band .gap {
    width: 3px;
    background: var(--charcoal);
  }
  .footer-band .rule {
    flex: 1;
    background: var(--grey);
  }
</style>
</head>
<body>
  <div class="business-card">
    <div class="smoke-decoration" role="img" aria-label="Faint rising smoke wisps curling into a spiral"></div>
    <div class="logo-divider"></div>
    <div class="brand-lockup">
      <h1 class="brand-name">The KestrA Nook</h1>
      <p class="brand-tagline">e-cigarette store</p>
    </div>
    <div class="footer-band">
      <div class="accent"></div>
      <div class="gap"></div>
      <div class="rule"></div>
    </div>
  </div>
</body>
</html>
```